Need Amazing Website for Consulting Company

We need an amazing website design for a Human Resources Consulting Company. This will be geared towards a more professional crowd, but we don't want it to be overly corporate and stuffy: Just, clean and professional and amazing. Please use the video link below for further instruction.

http://clipvesta.net/v/kqPzRmN4

Thank You.

PS Logo file has been attached.

Target Market(s)

The target marketing is small business owners who have employees. These owners cant afford an in-house HR person so they would hire this client to consult and do the work for them.

Industry/Entity Type

It Company

Font styles to use
Sans Serif

Requirements
Must have
• Please watch video:

Must have spot for video on homepage.
Nice to have
• Clean, professional, but not overly corporate, we want a personal and fun feel to this site a bit to separate them from all the other executive type sites. This site should have some LIFE to it and reflect a local brand that is doing great things.
Should not have
• Should not be just a corporate site, should not be overly stuffy, should not be overly boring.

```html
<!DOCTYPE html>
<html lang="en">
<head>
<meta charset="utf-8">
<title>Mesa Ridge HR Consulting</title>
<link href="https://fonts.googleapis.com/css2?family=Noto+Serif:ital,wght@0,400;0,700;1,400&family=Open+Sans:ital,wght@0,400;0,600;0,700;1,400&display=swap" rel="stylesheet">
<style>
:root{
  --red:#c4203a;
  --red-dark:#a3152c;
  --ink:#1e1e1e;
  --text:#333;
  --muted:#8a8a8a;
  --line:#e3e3e3;
  --card:#ececec;
  --footer:#323232;
  --white:#fff;
}
*{box-sizing:border-box;margin:0;padding:0}
html,body{width:972px;height:1200px;overflow:hidden;background:var(--white)}
body{position:relative;font-family:"Open Sans",sans-serif;color:var(--text)}
.abs{position:absolute}
.topline{left:0;top:0;width:972px;height:4px;background:var(--red)}
.header-bg{left:0;top:4px;width:972px;height:360px;background:linear-gradient(#fff 0%,#f4f4f4 40%,#ececec 100%)}

.brand{left:140px;top:20px;display:flex;align-items:center;gap:10px}
.brand-name{font-family:"Noto Serif",serif;font-weight:700;font-size:21px;line-height:25px;color:var(--ink)}
.brand-dot{width:22px;height:22px;border-radius:50%;background:var(--red)}

.phone{left:678px;top:13px;display:flex;align-items:center;gap:10px;color:var(--red);font-size:22px}
.quote-btn{left:678px;top:48px;width:155px;height:34px;border-radius:4px;background:linear-gradient(#4a4a4a,#151515);color:var(--white);font-weight:600;font-size:16px;display:flex;align-items:center;justify-content:center}

.nav{left:354px;top:93px;width:479px;height:34px;background:linear-gradient(#d8324c,var(--red-dark));border-radius:3px;display:flex;align-items:center;justify-content:space-around;list-style:none}
.nav li{color:var(--white);font-size:11px;font-weight:600}

.hero{left:139px;top:128px;width:694px;height:234px;clip-path:ellipse(75% 100% at 50% 100%);background:linear-gradient(100deg,#e9ecef 0%,#d7dbde 45%,#b5a69a 70%,#6c6f7a 100%)}
.hero-text{left:218px;top:206px;font-family:"Noto Serif",serif;color:var(--ink)}
.hero-text .l1,.hero-text .l3{font-size:20px;line-height:24px}
.hero-text .l2{font-size:26px;line-height:26px;color:var(--red)}
.dots{left:223px;top:341px;display:flex;gap:3px}
.dots span{width:11px;height:11px;border-radius:50%;background:#555}
.dots span:first-child{background:var(--red)}

.card{top:388px;width:222px;height:160px}
.card-body{position:absolute;left:0;top:14px;width:222px;height:146px;background:repeating-linear-gradient(90deg,#efefef 0 2px,#e9e9e9 2px 4px)}
.card-head{position:absolute;left:12px;top:12px;width:198px;height:36px;background:var(--white);border-radius:18px;display:flex;align-items:center;gap:8px;padding-left:12px;font-family:"Noto Serif",serif;font-size:21px;color:var(--ink);box-shadow:0 1px 2px rgba(0,0,0,.08)}
.card-cap{position:absolute;top:14px;width:22px;height:22px;border-radius:50%;background:var(--red)}
.card p{position:absolute;left:22px;top:78px;width:182px;font-size:9.5px;line-height:12px;color:var(--text)}
.card-arrow{position:absolute;right:0;bottom:0;width:38px;height:22px;background:var(--white);border-radius:19px 19px 0 0;display:flex;align-items:center;justify-content:center}

.section-title{font-family:"Noto Serif",serif;font-size:18px;color:var(--red)}
.section-title small{font-size:11px}
.rule{height:3px;background:var(--line)}
.welcome p{font-size:9.5px;line-height:12.2px;color:var(--muted);width:458px;margin-bottom:12px}

.video{left:611px;top:610px;width:222px;height:130px}
.video-screen{position:absolute;left:22px;top:0;width:178px;height:120px;border-radius:6px;background:#222;padding:7px}
.video-frame{width:100%;height:100%;background:linear-gradient(120deg,#dcd6cf,#8d9bb0 60%,#3e4c66)}
.video-base{position:absolute;left:0;top:120px;width:222px;height:8px;border-radius:0 0 8px 8px;background:linear-gradient(#e8e8e8,#b9b9b9)}

.testi-title{left:0;top:782px;width:972px;display:flex;align-items:center;justify-content:center}
.testi-line{position:absolute;top:792px;height:3px;background:var(--line)}
.ring{width:7px;height:7px;border:1.5px solid #777;border-radius:50%;margin:0 12px}

.quote-box{top:827px;width:323px;height:118px;background:repeating-linear-gradient(90deg,#efefef 0 2px,#eaeaea 2px 4px);padding:18px 13px}
.quote-box p{font-size:9.5px;line-height:14.8px;color:var(--text)}
.quote-tail{position:absolute;left:22px;bottom:-16px;width:0;height:0;border-left:10px solid transparent;border-top:16px solid #ececec}
.avatar{top:963px;width:44px;height:44px;border-radius:50%;background:linear-gradient(#bfb5aa,#5c5f6a);border:2px solid #ddd}
.author{top:968px;font-size:9.5px;line-height:15px}
.author em{color:var(--red)}

.footer{left:0;top:1041px;width:972px;height:130px;background:repeating-linear-gradient(90deg,#343434 0 2px,#2f2f2f 2px 4px)}
.footer h4{position:absolute;color:var(--white);font-size:11px;font-weight:700}
.footer .info{position:absolute;color:#ddd;font-size:9px;line-height:11px;display:flex;gap:10px}
.email-input{left:678px;top:1096px;width:155px;height:22px;background:linear-gradient(#fff,#e6e6e6);border-radius:3px;font-size:8px;color:#999;padding:6px 10px}
.socials{left:678px;top:1135px;display:flex;gap:12px}
.socials span{width:11px;height:11px;border-radius:2px;background:var(--white)}
.submit{left:776px;top:1130px;width:57px;height:19px;background:linear-gradient(#f23a4a,#c3101f);border-radius:3px;color:var(--white);font-size:10px;font-weight:700;display:flex;align-items:center;justify-content:center}

.bottom-bar{left:0;top:1171px;width:972px;height:29px;background:var(--red);color:#f3c6cd;font-size:8.5px}
.bottom-bar .copy{position:absolute;left:141px;top:9px}
.bottom-bar .links{position:absolute;right:139px;top:9px}
</style>
</head>
<body>
<div class="abs topline"></div>
<div class="abs header-bg"></div>

<div class="abs brand">
  <div class="brand-name">Mesa Ridge HR<br>Consulting</div>
  <span class="brand-dot"></span>
</div>

<div class="abs phone">
  <svg width="16" height="16" viewBox="0 0 16 16"><circle cx="8" cy="8" r="7" fill="none" stroke="#c4203a" stroke-width="1.6"/><path d="M5 4.5l1.6-.3.8 2-1 .8a5 5 0 0 0 2.6 2.6l.8-1 2 .8-.3 1.6c-3.4.4-6.9-3.1-6.5-6.5z" fill="#c4203a"/></svg>
  <span>555 01 23 45</span>
</div>
<div class="abs quote-btn">Request a Quote</div>

<ul class="abs nav">
  <li>Home</li><li>About Us</li><li>Seminars</li><li>Workshops</li><li>Meet our team</li><li>Contact us</li>
</ul>

<div class="abs hero" role="img" aria-label="Bright office with a smiling team of five business people"></div>
<div class="abs hero-text">
  <div class="l1">Without an</div>
  <div class="l2">INFRASTRUCTURE</div>
  <div class="l3">You are just not Social</div>
</div>
<div class="abs dots"><span></span><span></span><span></span></div>

<div class="abs card" style="left:139px">
  <div class="card-body"></div>
  <div class="card-head">
    <svg width="20" height="20" viewBox="0 0 20 20"><circle cx="8" cy="11" r="5" fill="none" stroke="#1e1e1e" stroke-width="3" stroke-dasharray="2.5 1.5"/><circle cx="15" cy="5" r="3" fill="none" stroke="#1e1e1e" stroke-width="2" stroke-dasharray="1.5 1"/></svg>
    Services
  </div>
  <span class="card-cap" style="left:0"></span><span class="card-cap" style="right:0"></span>
  <p>Mauris ac felis non sem pulvinar porttitor et ut lacus. Donec laoreet quam nisi, quis fauci bus enim tempor vel. Duis rutrum est enim, et varius quam scelerisque at. Nunc sodales sapien nec</p>
  <div class="card-arrow"><svg width="10" height="10" viewBox="0 0 10 10"><path d="M1 5h7M5 1.5L8.5 5 5 8.5" stroke="#c4203a" stroke-width="2" fill="none"/></svg></div>
</div>

<div class="abs card" style="left:375px">
  <div class="card-body"></div>
  <div class="card-head">
    <svg width="20" height="20" viewBox="0 0 20 20"><path d="M10 2l8 6-8 6-8-6z" fill="#1e1e1e"/><path d="M2 11l8 6 8-6" stroke="#1e1e1e" stroke-width="2" fill="none"/><path d="M6 8l3 2 5-4" stroke="#fff" stroke-width="1.5" fill="none"/></svg>
    Standards
  </div>
  <span class="card-cap" style="left:0"></span><span class="card-cap" style="right:0"></span>
  <p>Mauris ac felis non sem pulvinar porttitor et ut lacus. Donec laoreet quam nisi, quis fauci bus enim tempor vel. Duis rutrum est enim, et varius quam scelerisque at. Nunc sodales sapien nec</p>
  <div class="card-arrow"><svg width="10" height="10" viewBox="0 0 10 10"><path d="M1 5h7M5 1.5L8.5 5 5 8.5" stroke="#c4203a" stroke-width="2" fill="none"/></svg></div>
</div>

<div class="abs card" style="left:611px">
  <div class="card-body"></div>
  <div class="card-head">
    <svg width="18" height="20" viewBox="0 0 18 20"><circle cx="9" cy="6" r="5" fill="#1e1e1e"/><path d="M0 20c0-6 4-8 9-8s9 2 9 8z" fill="#1e1e1e"/></svg>
    Work with Us
  </div>
  <span class="card-cap" style="left:0"></span><span class="card-cap" style="right:0"></span>
  <p>Mauris ac felis non sem pulvinar porttitor et ut lacus. Donec laoreet quam nisi, quis fauci bus enim tempor vel. Duis rutrum est enim, et varius quam scelerisque at. Nunc sodales sapien nec</p>
  <div class="card-arrow"><svg width="10" height="10" viewBox="0 0 10 10"><path d="M1 5h7M5 1.5L8.5 5 5 8.5" stroke="#c4203a" stroke-width="2" fill="none"/></svg></div>
</div>

<h2 class="abs section-title" style="left:141px;top:579px">Welcome to Mesa Ridge Consulting <small>LLC.</small></h2>
<div class="abs rule" style="left:139px;top:603px;width:458px"></div>
<div class="abs welcome" style="left:141px;top:617px">
  <p>Mauris ac felis non sem pulvinar porttitor et ut lacus. Donec laoreet quam nisi, quis faucibus enim tempor vel. Duis rutrum est enim, et varius quam scelerisque at. Nunc sodales sapien nec tellus vehicula, nec congue massa ultricies. Aliquam eleifend et odio eu accumsan. Maecenas rhoncus, lorem nec dictum placerat, magna tortor mattis mi, mollis euismod justo sapien nec sem. Nullam vitae aliquet arcu, quis malesuada purus.</p>
  <p>Aenean in tincidunt lectus. Nullam eget rutrum nunc. Duis commodo quis massa eget condimentum. Suspendisse id leo commodo, lobortis sapien eu, tristique lacus. Nulla interdum quis justo eu porttitor. Donec vitae mi nec purus hendrerit vulputate. In et posuere lectus. Morbi vitae orci hendrerit, cursus tortor eu, tristique risus. Curabitur congue, dui eget ultricies sagittis, enim ante tempus sapien, ac ullamcorper odio tortor eu nisi. Vestibulum eget orci id erat pretium volutpat in in magna. Lorem ipsum dolor sit amet, consectetur adipiscing elit. Aliquam viverra, tellus non interdum cursus, nibh dolor aliquam mi, eget tincidunt libero augue aliquet quam. A</p>
</div>

<h2 class="abs section-title" style="left:612px;top:579px">Our Video</h2>
<div class="abs rule" style="left:611px;top:603px;width:222px"></div>
<div class="abs video">
  <div class="video-screen"><div class="video-frame" role="img" aria-label="Video still of a business meeting with a handshake"></div></div>
  <svg class="abs" style="left:100px;top:50px" width="22" height="24" viewBox="0 0 22 24"><path d="M2 2l18 10-18 10z" fill="rgba(255,255,255,.8)"/></svg>
  <div class="video-base"></div>
</div>

<div class="abs testi-line" style="left:139px;width:265px"></div>
<div class="abs testi-line" style="left:567px;width:266px"></div>
<div class="abs testi-title"><span class="ring"></span><span class="section-title">Testimonials</span><span class="ring"></span></div>

<div class="abs quote-box" style="left:139px">
  <p>Nam volutpat euismod massa quis faucibus. Cras vitae risus nec neque egestas sagittis sed id risus. Phasellus id quam vitae magna ullamcorper tincidunt. Phasellus eleifend dictum sem, eget ultrices odio commodo id. Aliquam ultricies eu lacus sit amet bibendum. Vivamus ac magna ante. Fusce nisi ligula, volutpat non venenatis id, facilisis ut odio.</p>
  <span class="quote-tail"></span>
</div>
<div class="abs quote-box" style="left:511px">
  <p>Nam volutpat euismod massa quis faucibus. Cras vitae risus nec neque egestas sagittis sed id risus. Phasellus id quam vitae magna ullamcorper tincidunt. Phasellus eleifend dictum sem, eget ultrices odio commodo id. Aliquam ultricies eu lacus sit amet bibendum. Vivamus ac magna ante. Fusce nisi ligula, volutpat non venenatis id, facilisis ut odio.</p>
  <span class="quote-tail"></span>
</div>

<div class="abs avatar" style="left:152px" role="img" aria-label="Portrait of a male client"></div>
<div class="abs author" style="left:206px"><em>Nullam eget rutrum</em><br>ac ullamcorper odio tortor eu nisi</div>
<div class="abs avatar" style="left:528px" role="img" aria-label="Portrait of a female client"></div>
<div class="abs author" style="left:588px"><em>Nullam eget rutrum</em><br>ac ullamcorper odio tortor eu nisi</div>

<footer class="abs footer">
  <h4 style="left:141px;top:32px">Contact Info</h4>
  <div class="info" style="left:139px;top:58px">
    <svg width="12" height="12" viewBox="0 0 12 12"><path d="M6 1L0 6h2v5h3V8h2v3h3V6h2z" fill="#fff"/></svg>
    <span>In et posuere lectus. Morbi vitae orci<br>hendrerit, cursus tortor eu,</span>
  </div>
  <div class="info" style="left:345px;top:59px">
    <svg width="11" height="12" viewBox="0 0 11 12"><path d="M1 1l3-.5 1.2 3-1.5 1a6 6 0 0 0 3 3l1-1.5 3 1.2L10 11C5 11 1 6 1 1z" fill="#fff"/></svg>
    <span>Houston: 555 01 23 45</span>
  </div>
  <div class="info" style="left:483px;top:59px">
    <svg width="12" height="9" viewBox="0 0 12 9"><rect width="12" height="9" fill="#fff"/><path d="M0 0l6 5 6-5" stroke="#333" fill="none"/></svg>
    <span>info@mesaridge-hr.example</span>
  </div>
  <h4 style="left:678px;top:32px">Subscribe Newsletter</h4>
</footer>
<div class="abs email-input">Enter email address</div>
<div class="abs socials" aria-label="Social links"><span></span><span></span><span></span><span></span></div>
<div class="abs submit">Submit</div>

<div class="abs bottom-bar">
  <span class="copy">Copyright © 2014, All rights reserved.</span>
  <span class="links">Home &nbsp;|&nbsp; About Us &nbsp;|&nbsp; Seminars &nbsp;|&nbsp; Workshops &nbsp;|&nbsp; Meet our team &nbsp;|&nbsp; Contact us</span>
</div>
</body>
</html>
```